Veranaxis Business Card and Letter Head

We are a leadership assessment consultancy based in Sydney, Australia. We help executive-level decison-makers select leaders for more senior level roles in corporate and government organisations. Our methodology is based on the latest research from the field of neuroscience.
We need a business card design and matching letter head that presents our company, Veranaxis, as a:
1. trusted adviser to senior executive-level decison makers
2. niche consultancy who are experts in the field of assessing leadership talent
3. results-focused solution provider who balance scientific methods with pragmatic solutions
The following company details should be used in all designs:
Company Name: Veranaxis
Details (for business card):
Daniel Prescott
High Potential Officer
Level 29, Brenning Tower
7 Brenning Square
Sydney, NSW 2000 Australia
Phone: 1300 482 716
Mobile: 0412 573 208
Email: daniel.prescott@veranaxis.com.au
Website: veranaxis.com.au
I have attached the logo for Veranaxis (for both a white and black background) - your business card and letter head designs must incoporate this logo and colour scheme.
Thanks for your interest in this project, I'm looking forward to receiving your ideas.
Regards,
Daniel
Executive-level decison-makers in corporate and government organisations (e.g., CEO, VP, Head of Human Resources)
Leadership

```html
<!DOCTYPE html>
<html lang="en">
<head>
<meta charset="utf-8">
<title>Veranaxis – Business Card Options</title>
<link rel="stylesheet" href="https://fonts.googleapis.com/css2?family=Oswald:wght@300;400&display=swap">
<style>
  :root {
    --paper: #ffffff;
    --ink: #3a3a3a;
    --charcoal: #363636;
    --brand-red: #c0301f;
    --card-edge: #1e1e1e;
    --soft-ink: #f2f2f2;
  }
  * { box-sizing: border-box; margin: 0; padding: 0; }
  html, body {
    width: 1200px;
    height: 869px;
    overflow: hidden;
    background: var(--paper);
  }
  .sheet {
    position: relative;
    width: 1200px;
    height: 869px;
    font-family: "Oswald", "Arial Narrow", sans-serif;
    color: var(--ink);
  }
  .option-label {
    position: absolute;
    top: 28px;
    font-size: 25px;
    font-weight: 300;
    color: var(--ink);
    letter-spacing: 0.2px;
  }
  .option-label--one { left: 139px; }
  .option-label--two { left: 612px; }
  .sheet-caption {
    position: absolute;
    right: 162px;
    top: 794px;
    font-size: 25px;
    font-weight: 300;
    color: var(--ink);
  }

  .card {
    position: absolute;
    top: 94px;
    width: 428px;
    height: 686px;
    background: var(--paper);
    border: 1px solid var(--card-edge);
    overflow: hidden;
  }
  .card--one { left: 136px; }
  .card--two { left: 609px; }

  .wordmark {
    position: absolute;
    font-weight: 400;
    color: var(--ink);
    letter-spacing: 1px;
    white-space: nowrap;
    line-height: 1;
  }
  .card--one .wordmark {
    left: 69px;
    top: 225px;
    font-size: 66px;
    transform: translate(-50%, -50%) rotate(-90deg);
  }
  .card--two .wordmark {
    left: 50px;
    top: 88px;
    font-size: 62px;
  }

  .brand-block {
    position: absolute;
    background: var(--charcoal);
  }
  .card--one .brand-block {
    left: 220px;
    top: 68px;
    width: 145px;
    height: 142px;
  }

  .holder {
    position: absolute;
    font-size: 29px;
    font-weight: 400;
    line-height: 1.42;
    color: var(--brand-red);
    letter-spacing: -0.2px;
  }
  .card--one .holder { left: 220px; top: 311px; }
  .card--two .holder { left: 193px; top: 280px; }

  .contact-band {
    position: absolute;
    left: 0;
    right: 0;
    bottom: 0;
  }
  .card--one .contact-band {
    top: 523px;
    background: var(--brand-red);
  }
  .card--two .contact-band {
    top: 384px;
    background: var(--charcoal);
  }

  .contact {
    position: absolute;
    font-size: 13px;
    font-weight: 300;
    line-height: 1.6;
    color: var(--soft-ink);
    white-space: nowrap;
    letter-spacing: -0.1px;
  }
  .card--one .contact--address { left: 52px; top: 30px; }
  .card--one .contact--lines { left: 220px; top: 30px; }
  .card--two .contact--address { left: 205px; top: 106px; }
  .card--two .contact--lines { left: 207px; top: 180px; }

  .corner-square {
    position: absolute;
    left: 10px;
    top: 90px;
    width: 56px;
    height: 56px;
    background: var(--charcoal);
  }

  .badge-square {
    position: absolute;
    left: 18px;
    top: 321px;
    width: 137px;
    height: 127px;
    background: var(--paper);
  }
</style>
</head>
<body>
<main class="sheet">
  <p class="option-label option-label--one">option 1</p>
  <p class="option-label option-label--two">option 2</p>

  <section class="card card--one" aria-label="Business card, option 1">
    <p class="wordmark">Veranaxis</p>
    <div class="brand-block" aria-hidden="true"></div>
    <p class="holder">Daniel Prescott<br>High Potential Officer</p>
    <div class="contact-band">
      <p class="contact contact--address">Level 29, Brenning Tower<br>7 Brenning Square<br>Sydney, NSW 2000 Australia</p>
      <p class="contact contact--lines">Phone: 1300 482 716<br>Mobile: 0412 573 208<br>Email: daniel.prescott@veranaxis.com.au<br>Website: veranaxis.com.au</p>
      <div class="corner-square" aria-hidden="true"></div>
    </div>
  </section>

  <section class="card card--two" aria-label="Business card, option 2">
    <p class="wordmark">Veranaxis</p>
    <p class="holder">Daniel Prescott<br>High Potential Officer</p>
    <div class="contact-band">
      <p class="contact contact--address">Level 29, Brenning Tower<br>7 Brenning Square<br>Sydney, NSW 2000 Australia</p>
      <p class="contact contact--lines">Phone: 1300 482 716<br>Mobile: 0412 573 208<br>Email: daniel.prescott@veranaxis.com.au<br>Website: veranaxis.com.au</p>
    </div>
    <div class="badge-square" aria-hidden="true"></div>
  </section>

  <p class="sheet-caption">business cards</p>
</main>
</body>
</html>
```